$5 Venture Website Required

I am looking for someone to develop a website akin to the simplicity of www.filetrove.net with a video in the center or a tab that permits one to "Accept the Challenge."

Incorporates our logo and is used to promote our "$5 Venture Program."

Please see attachments, but we are igniting entrepreneurial spirit among our nation's youth through this interactive and intensive program!

There should be a way to navigate to other sections of the site including:

About
Why
Request $5 Venture Packet
Success Stories
Partners
Link to Morvan Holdings
Updates

Thanks to all in advance!

Looking forward to working with you!

Good feel of what we are looking for in terms of "feel"

http://www.brightpathwave.org/

Thank you,

RK

Please make note of this website, we are going for a feel that is akin to this and less modern and professional...more abstract and interactive...but of course include space for our video:

Colors, feel, imagery, is great. Keep your formats, but bring on the feel!

Thank you all for your hard work and patience.

Thank you all for your hard work thus far.

Meanwhile, please understand that the $5 Venture is young, youthful, full of challenge and vitality, it is a competition among students from high school and universities.  The websites you have delivered are too corporate, stale, and standard.  I'm looking for something that is fresh, different, like www.brightpathwave.org.

Symbols, cartoonish, but serious, down to business and save the world one $5 bill at a time.  The logo can be used as a theme...the colors, the feel.

Video space for explanation on the $5 Venture front and center.  With leaves, $ signs, colorful colors, etc.

Visual needs to be compelling to Join the Challenge! Although Morvan Holdings and the tree is a parent company; $5 Venture is separate and Morvan Holdings should only be mentioned as a link.

SketchHive.com in regard to simplicity; and www.brightpathwave.org in terms of style.

Thank you,

Ravinder

Like the designs that have been submitted; we are almost there.

Target Market(s)

Professors, students, teachers, parents and NGO leaders who wish to use our program as a way to inspire leadership/entrepreneurship/fundraise for their causes.

Requirements
Must have
• Place for the video, front and center
Include logo
Forsight for blogging, message, etc.
Nice to have
• Plan "buckets" to include"
Explanation Video
Two pamphlets
Contract
FAQs
Website with Blog, voting, registration, video upload, etc.
Flyer perfected
Parable...symbol of our life
Photos
Stats included
Testimonials
Organizations that have used (TLWMB, Lower Mill Forum, Corbridge High)
Sponsors (Vast Signal, Quillstone Learnerhouse)
Photos from events

I understand this takes coding and such, but want you to be aware of the long term vision for it!

```html
<!DOCTYPE html>
<html lang="en">
<head>
<meta charset="utf-8">
<title>$5 Venture</title>
<link rel="stylesheet" href="https://fonts.googleapis.com/css2?family=Mulish:wght@400;700;800&family=Arimo:wght@400;700&display=swap">
<style>
:root{
  --green:#1f9447;
  --green-dark:#137a36;
  --green-text:#2a9a3e;
  --ink:#333333;
  --muted:#555555;
  --bar:#3b3b3b;
  --panel:#f1f1f1;
  --line:#d4d4d4;
  --link:#0a7a2f;
  --blue:#2a8ad4;
  --white:#ffffff;
}
*{margin:0;padding:0;box-sizing:border-box}
html,body{width:740px;height:1200px;overflow:hidden;background:var(--white)}
body{position:relative;font-family:"Arimo",Arial,sans-serif;color:var(--ink);font-size:10px}
.abs{position:absolute}

.brand{left:46px;top:20px;display:flex;align-items:center;gap:8px}
.brand-dot{width:26px;height:26px;border-radius:50%;background:var(--green)}
.brand-name{font-family:"Mulish",sans-serif;font-weight:800;font-size:26px;color:var(--green-dark)}

.hero-bg{left:0;top:80px;width:740px;height:460px;background:linear-gradient(180deg,#efefef 0%,#e4e4e4 40%,#d9d4cc 80%,#cfc7bb 100%)}
.video{left:95px;top:103px;width:550px;height:294px;border:2px solid #444;background:linear-gradient(180deg,#d8dcd9 0%,#c6c9c2 45%,#8d6a4c 75%,#6b5040 100%)}
.play{left:334px;top:218px;width:68px;height:68px;border-radius:50%;background:rgba(30,30,30,.82);display:flex;align-items:center;justify-content:center}

.band{left:0;top:420px;width:740px;height:80px;background:var(--green);border-top:2px solid #2fb35a;border-bottom:2px solid #0f6b2c}
.field{height:20px;background:var(--white);border:1px solid #bbb;font-size:9px;color:#999;padding:4px 6px}
.login{left:188px;top:433px;width:54px;height:52px;background:var(--green-dark);border:1px solid #0b5a24;color:var(--white);font-family:"Mulish",sans-serif;font-weight:700;font-size:10px;display:flex;align-items:center;justify-content:center}
.forgot{left:47px;top:487px;font-size:8.5px;color:#dff3e4}
.forgot span{color:#f2f27a;margin-left:14px}
.divider{top:426px;width:1px;height:68px;background:#5bc27d}
.search{left:403px;top:447px;width:56px;height:22px;background:var(--green-dark);border:1px solid #0b5a24;color:var(--white);font-family:"Mulish",sans-serif;font-weight:700;font-size:10px;display:flex;align-items:center;justify-content:center}
.follow{left:484px;top:430px;font-size:11px;color:var(--white)}
.socials{left:484px;top:456px;display:flex;gap:11px}
.social{width:30px;height:32px;border-radius:3px;background:#f4f4f4;border:1px solid #0b5a24}

.nav{left:0;top:539px;width:740px;height:32px;background:var(--bar);font-weight:700;font-size:10px;color:var(--white)}
.nav span{position:absolute;top:10px}

.col{top:590px;width:210px}
.col-head{display:flex;align-items:center;gap:8px;margin-bottom:6px}
.col-icon{width:22px;height:26px;border-radius:3px}
.col-title{font-family:"Mulish",sans-serif;font-weight:700;font-size:13px;color:var(--green-text)}
.col p{font-size:8.6px;line-height:15px;color:var(--muted)}
.more{color:var(--blue)}

.panel{left:0;top:760px;width:740px;height:370px;background:var(--panel)}
.card{background:var(--white);border-left:4px solid #cfcfcf;box-shadow:0 0 2px rgba(0,0,0,.12);padding:10px 12px 0 12px;overflow:hidden}
.card-icon{position:absolute;left:-4px;top:-6px;width:30px;height:30px}
.card-title{position:absolute;right:10px;top:12px;font-weight:700;font-size:10px;color:#222}
.card-links{position:absolute;left:4px;top:54px;font-size:9px;line-height:16px}
.card-links a{display:block;color:var(--link);text-decoration:underline}
.round{position:absolute;border-radius:50%;border:3px solid #e8e8e8}
.quote{font-size:9px;line-height:15px;color:var(--muted)}
.t-quote{font-size:8.6px;line-height:14px;color:var(--muted)}
.author{text-align:right;color:var(--green-text);font-size:8.6px;margin:1px 0 5px;border-bottom:1px solid var(--line);padding-bottom:3px}
.q-head{font-weight:700;font-size:10px;color:#222;margin-bottom:2px}
.small-meta{display:flex;justify-content:space-between;font-size:8px;margin-bottom:6px}
.small-meta span:first-child{color:var(--green-text)}
.vote-q{font-size:9px;line-height:14px;color:#222;margin-bottom:4px}
.opt{display:flex;align-items:center;gap:6px;font-size:9px;color:var(--muted);margin-bottom:5px}
.radio{width:10px;height:10px;border:1px solid #aaa;border-radius:50%}
.vote-btn{display:inline-block;background:var(--green);color:var(--white);font-weight:700;font-size:9px;padding:3px 7px;border-radius:2px}

.footer{left:0;top:1142px;width:740px;height:31px;background:var(--bar);color:var(--white);font-size:9.5px;display:flex;align-items:center;padding-left:46px}
.copy{left:46px;top:1180px;font-size:8.5px;color:#666}
</style>
</head>
<body>

<div class="abs brand"><span class="brand-dot"></span><span class="brand-name">$5 Venture</span></div>

<div class="abs hero-bg" role="img" aria-label="Soft blurred classroom backdrop"></div>
<div class="abs video" role="img" aria-label="Video still of a teacher at a whiteboard with students raising hands"></div>
<div class="abs play"><svg width="28" height="30" viewBox="0 0 28 30"><path d="M4 2 L26 15 L4 28 Z" fill="#fff"/></svg></div>

<div class="abs band"></div>
<div class="abs field" style="left:47px;top:433px;width:130px">Email Address</div>
<div class="abs field" style="left:47px;top:463px;width:130px">Password</div>
<div class="abs login">LOGIN</div>
<div class="abs forgot">Forgot Password?<span>Dont have login? Click Here</span></div>
<div class="abs divider" style="left:252px"></div>
<div class="abs field" style="left:263px;top:448px;width:130px">Email Address</div>
<div class="abs search">Search</div>
<div class="abs divider" style="left:470px"></div>
<div class="abs follow">Follow Us</div>
<div class="abs socials">
  <span class="social"></span><span class="social"></span><span class="social"></span><span class="social"></span>
  <span class="social" style="display:flex;align-items:center;justify-content:center"><svg width="18" height="14" viewBox="0 0 18 14"><rect x="1" y="1" width="16" height="12" fill="none" stroke="#555" stroke-width="1.5"/><path d="M1 1 L9 8 L17 1" fill="none" stroke="#555" stroke-width="1.5"/></svg></span>
</div>

<nav class="abs nav">
  <span style="left:55px">About</span>
  <span style="left:137px">Why</span>
  <span style="left:205px">Request $5 Venture Packet</span>
  <span style="left:385px">Success Stories</span>
  <span style="left:483px">Partners</span>
  <span style="left:577px">Link to Morvan Holdings</span>
</nav>

<section class="abs col" style="left:49px">
  <div class="col-head"><span class="col-icon" style="background:#1d6fc2"></span><span class="col-title">About 5 $ Venture</span></div>
  <p>A recent phenomenon, lead by social enterprise Morvan Holdings in collaboration with Quillstone Learnerhouse and Halloway University, called "The Five Coin Quest" is sweeping across high school and student entrepreneurship organizations across the country and challenging students to put their entrepreneurial genius to work in order to multiply their "$5 Spark Factor" as many</p>
</section>
<section class="abs col" style="left:267px">
  <div class="col-head"><span class="col-icon" style="background:#e8742a;border-radius:50%;width:24px;height:24px"></span><span class="col-title">Blog</span></div>
  <p>A recent phenomenon, lead by social enterprise Morvan Holdings <span class="more">More...</span><br>A recent phenomenon, lead by social enterprise Morvan Holdings <span class="more">More...</span><br>&nbsp;A recent phenomenon, lead by social enterprise Morvan Holdings <span class="more">More...</span><br>A recent phenomenon, lead by social enterprise Morvan Holdings <span class="more">More...</span></p>
</section>
<section class="abs col" style="left:485px">
  <div class="col-head"><span class="col-icon" style="background:#f0a21c"></span><span class="col-title">Success Story</span></div>
  <p>A recent phenomenon, lead by social enterprise Morvan Holdings in collaboration with Quillstone Learnerhouse and Halloway University, called "The Five Coin Quest" is sweeping across high school and student entrepreneurship organizations across the country and challenging students to put their entrepreneurial genius to work in order to multiply their "$5 Spark Factor" as many</p>
</section>

<div class="abs panel"></div>

<div class="abs card" style="left:53px;top:784px;width:207px;height:153px">
  <svg class="card-icon" viewBox="0 0 30 30"><circle cx="15" cy="15" r="14" fill="#222"/><rect x="7" y="11" width="11" height="9" fill="#fff"/><path d="M18 15 L24 11 L24 20 Z" fill="#fff"/></svg>
  <div class="card-title">VIDEO</div>
  <div class="card-links"><a>View Video</a><a>Upload Video</a><a>Search Video</a><a>Search Event Video</a></div>
  <div class="round" role="img" aria-label="Round photo of a teacher with students" style="left:88px;top:20px;width:106px;height:106px;background:linear-gradient(160deg,#cfd8e6,#8a9cb8)"></div>
</div>
<div class="abs card" style="left:267px;top:784px;width:206px;height:153px">
  <svg class="card-icon" viewBox="0 0 30 30"><rect x="2" y="4" width="26" height="22" rx="2" fill="#f2f2f2" stroke="#999"/><path d="M4 22 L11 13 L16 19 L20 15 L26 22 Z" fill="#3a9a3a"/><circle cx="21" cy="9" r="3" fill="#f0b020"/></svg>
  <div class="card-title">PHOTO</div>
  <div class="card-links"><a>View Photo</a><a>Upload Photo</a><a>Search Photo</a><a>Search Event Photo</a></div>
  <div class="round" role="img" aria-label="Round photo of a group of business people" style="left:84px;top:20px;width:110px;height:110px;background:linear-gradient(160deg,#e4e4e4,#7e8ea3)"></div>
</div>
<div class="abs card" style="left:483px;top:784px;width:206px;height:153px;padding-top:28px">
  <svg class="card-icon" viewBox="0 0 30 30"><rect x="3" y="3" width="20" height="24" fill="#fdf6d8" stroke="#bbb"/><path d="M10 24 L25 6 L28 9 L13 27 Z" fill="#f0a21c"/></svg>
  <div class="card-title">TESTIMONIAL</div>
  <div class="t-quote">A recent phenomenon, lead by social Morvan Holdings in collaboration with Quillstone Learnerhouse</div>
  <div class="author">- Daniel Corwen</div>
  <div class="t-quote">A recent phenomenon, lead by social Morvan Holdings in collaboration with Quillstone Learnerhouse</div>
  <div class="author" style="border:0">- Daniel Corwen</div>
</div>

<div class="abs card" style="left:53px;top:949px;width:207px;height:160px;padding-top:46px">
  <svg class="card-icon" viewBox="0 0 30 30"><circle cx="15" cy="15" r="14" fill="#1f6b2f"/><rect x="8" y="9" width="14" height="2" fill="#fff"/><rect x="8" y="14" width="14" height="2" fill="#fff"/><rect x="8" y="19" width="10" height="2" fill="#fff"/></svg>
  <div class="card-title" style="top:18px">ARTICLE</div>
  <div class="q-head">Are You Ready for 5 $ Venture?</div>
  <div class="small-meta"><span>In Daily Ledger</span><span>28th Oct,2012</span></div>
  <div class="quote">A recent phenomenon, lead by social Morvan Holdings in collaboration with Quill<br>A recent phenomenon, lead by social Morvan Holdings in collaboration with Quill</div>
</div>
<div class="abs card" style="left:267px;top:949px;width:206px;height:160px;padding-top:46px">
  <svg class="card-icon" viewBox="0 0 30 30"><circle cx="15" cy="15" r="14" fill="#1d8bc9"/><path d="M11 11 Q11 7 15 7 Q19 7 19 11 Q19 14 15 15 L15 18" fill="none" stroke="#fff" stroke-width="2.5"/><circle cx="15" cy="22" r="1.6" fill="#fff"/></svg>
  <div class="card-title" style="top:18px">FAQs</div>
  <div class="q-head">Are You Ready for 5 $ Venture?</div>
  <div class="quote">A recent phenomenon, lead by social more<br>A recent phenomenon, lead by social &nbsp;more</div>
  <div class="q-head" style="margin-top:8px">Are You Ready for 5 $ Venture?</div>
  <div class="quote">A recent phenomenon, lead by social faqs<br>A recent phenomenon, lead by social faqs</div>
</div>
<div class="abs card" style="left:483px;top:949px;width:206px;height:160px;padding-top:42px">
  <svg class="card-icon" viewBox="0 0 30 30"><circle cx="15" cy="15" r="14" fill="#2e9a3e"/><path d="M9 14 L13 14 L16 7 Q18 7 18 10 L17 13 L22 13 Q24 14 23 16 L21 22 L9 22 Z" fill="#fff"/></svg>
  <div class="card-title" style="top:18px">VOTE</div>
  <div class="vote-q">What is the shape of the perfect leader and does he or she exist?</div>
  <div class="opt"><span class="radio"></span>A vision of the future</div>
  <div class="opt"><span class="radio"></span>Rude Altitude</div>
  <div class="opt"><span class="radio"></span>Talkaive Nature</div>
  <span class="vote-btn">Vote</span>
</div>

<footer class="abs footer">About &nbsp;|&nbsp; Why &nbsp;|&nbsp; Request $5 Venture Packet &nbsp;|&nbsp; Success Stories &nbsp;|&nbsp; Patners &nbsp;|&nbsp; Link to Morvan Holdings</footer>
<div class="abs copy">© Copyright 2005 $5 Venture | Privacy Policy</div>

</body>
</html>
```